South Florida Real Estate Brokerage Business

The name is DWELL VANTORO REAL ESTATE.
The company is a Real estate realty based in Miami.
Is targeted to Latin American clients.
Must express luxury, and efficiency.
Target clients for properties around 250k to a million +.
Vantoro means Royal in Latin.
Should communicate safety and knowledge of the product and transaction with a tech edge.

The web design needs to be a Social tool, with Chatterloop and other media integration of some sort. Needs to have a Show case place, a Search place (MLS listings) with maps and filters.
Needs to reflect luxury but also mixed with a social edge capable of engaging clients or transition them to communicate with the page.
Include the logo from the uploaded files, feel free to change the color or font per webdesign.
This is a Front en design, layout and graphics.
Possible future programming if approved.
I can receive Quotes for the Code part.

Target Market(s)

Spanish and English speakers living in Latin America and Canada looking for apartments and houses to buy.

Industry/Entity Type

Business

Requirements
Must have
• Search area.
Neighbourhood area.
Could be a blog or news area.
Client registration.
Social Plugin
Nice to have
• Social linking to networks.
Log in with chatterloop account.
Chatterloop Like.

```html
<!DOCTYPE html>
<html lang="en">
<head>
<meta charset="utf-8">
<title>Dwell Vantoro Real Estate</title>
<link href="https://fonts.googleapis.com/css2?family=Ubuntu:wght@300;400;500;700&display=swap" rel="stylesheet">
<style>
:root{
  --gold:#c9a462;
  --gold-dark:#a8823f;
  --gold-text:#d79a2b;
  --ink:#1c1c1c;
  --bar:#191919;
  --text:#2b2b2b;
  --muted:#777;
  --page:#f0f0f0;
  --panel:#f3f3f3;
  --line:#d6d6d6;
  --link:#1e7a8c;
  --navy:#2d4f7c;
}
*{box-sizing:border-box;margin:0;padding:0}
html,body{width:968px;height:1200px;overflow:hidden}
body{font-family:"Ubuntu",sans-serif;color:var(--text);background:var(--page);position:relative;font-size:9px}
.abs{position:absolute}
.topline{left:0;top:0;width:968px;height:5px;background:var(--ink)}
.header{left:0;top:5px;width:968px;height:124px;background:linear-gradient(#f7f7f7,#e9e9e9)}
.brand{left:95px;top:36px;display:flex;align-items:center;gap:8px}
.brand-square{width:14px;height:14px;background:var(--gold)}
.brand-name{font-size:17px;font-weight:400;color:#333;letter-spacing:1px;line-height:1.2;width:160px}
.ask{left:671px;top:6px;width:208px;height:39px;border:1px solid #d0d0d0;background:#fafafa;border-radius:2px;padding:8px 0 0 14px;font-size:9.5px;line-height:1.25;color:#222}
.ask-btn{position:absolute;right:16px;top:10px;width:62px;height:17px;background:var(--gold);color:#fff;font-size:8.5px;text-align:center;line-height:17px;border-radius:2px}
.social-login{left:674px;top:66px;width:205px;height:34px;border-radius:4px;background:linear-gradient(#4a6c9c,#2e4d7a);color:#fff;display:flex;align-items:center;font-size:12.5px}
.social-login .sq{width:28px;height:34px;border-right:1px solid #5a7aa6;display:flex;align-items:center;justify-content:center}
.social-login .sq span{width:10px;height:10px;background:#fff}
.social-login b{font-weight:500;margin-left:4px}
.social-login .lbl{padding-left:12px}
.nav{left:0;top:129px;width:968px;height:32px;background:var(--bar)}
.nav-tab{left:95px;top:126px;width:63px;height:37px;background:var(--gold);color:#222;font-size:10.5px;text-align:center;line-height:37px;border-radius:2px}
.nav-item{top:129px;height:32px;line-height:32px;color:#fff;font-size:10.5px;transform:translateX(-50%)}
.search{left:707px;top:136px;width:156px;height:19px;border-radius:10px;background:#fff;overflow:hidden;font-size:8px;color:#aaa;padding-left:10px;line-height:19px}
.search-btn{position:absolute;right:0;top:0;width:24px;height:19px;background:#3d9c3a}
.hero{left:0;top:161px;width:968px;height:297px;background:linear-gradient(160deg,#6f8a9c 0%,#c9b9a2 35%,#8a7c63 60%,#3f5a2c 100%)}
.register{left:632px;top:181px;width:247px;height:267px;background:rgba(245,245,245,.93);border-radius:3px;overflow:hidden}
.register-head{height:35px;background:var(--bar);color:#fff;font-size:14px;line-height:35px;padding-left:57px;position:relative}
.register-head i{position:absolute;left:16px;top:9px;width:20px;height:17px;background:#c62c2c;border-radius:2px}
.field{position:absolute;left:12px;font-size:8px;color:#444}
.input{position:absolute;left:114px;width:128px;height:19px;border:1px solid #bfc8cf;border-radius:3px;background:#fff}
.check{position:absolute;left:13px;font-size:7.8px;color:#444;display:flex;align-items:center;gap:6px}
.check i{width:12px;height:12px;border:1px solid #999;background:#fff;display:block}
.check u{color:#222}
.reg-btn{position:absolute;left:65px;top:232px;width:121px;height:26px;background:var(--gold);color:#222;font-size:11.5px;text-align:center;line-height:26px;border:1px solid var(--gold-dark);border-radius:2px}
.ticker{left:0;top:458px;width:968px;height:37px;background:var(--bar);color:#fff;font-size:8.6px;line-height:12.5px;padding:6px 0 0 97px}
.ticker em{color:var(--gold-text);font-style:normal}
.like-btn{left:815px;top:468px;width:46px;height:17px;border:1px solid #aaa;background:#f4f4f4;font-size:9.5px;color:var(--navy);text-align:right;padding-right:5px;line-height:15px}
.like-btn i{position:absolute;left:5px;top:4px;width:8px;height:7px;border:1px solid var(--navy)}
.content{left:89px;top:495px;width:790px;height:663px;background:var(--panel);box-shadow:0 0 4px rgba(0,0,0,.15)}
.h-featured{left:108px;top:513px;font-size:15.5px;font-weight:300;color:#222}
.h-featured span{color:var(--gold-text)}
.arrow{top:576px;width:0;height:0;border-top:6px solid transparent;border-bottom:6px solid transparent}
.thumb{top:546px;width:139px;height:78px;border-radius:6px}
.cap{top:628px;font-size:9.5px;color:#222;line-height:12px}
.cap small{display:block;font-size:8.5px;color:var(--link)}
.fore{left:99px;top:679px;width:601px;height:178px;background:#f6f6f6;border:1px solid var(--line);border-radius:2px}
.fore-head{height:37px;background:var(--bar);color:#fff;font-size:13.5px;font-weight:500;line-height:40px;padding-left:32px;position:relative}
.fore-head i{position:absolute;left:12px;top:11px;width:16px;height:14px;background:#fff;border-radius:2px}
.fore-text{position:absolute;left:8px;top:46px;width:240px;font-size:8.5px;line-height:11.5px;color:#333}
.fin{position:absolute;left:8px;height:16px;border:1px solid #ccc;border-radius:3px;background:#fff;font-size:9px;color:#999;line-height:14px;padding-left:7px}
.fore-btn{position:absolute;left:8px;top:156px;width:48px;height:14px;background:var(--gold);font-size:8.5px;text-align:center;line-height:14px;border-radius:2px}
.divider{position:absolute;left:281px;top:45px;width:1px;height:120px;background:var(--line)}
.map{position:absolute;left:302px;top:45px;width:290px;height:119px;background:linear-gradient(90deg,#dcd7c5 0%,#e6e1d0 55%,#a9c8e4 57%,#9ec1e0 100%);border-radius:3px}
.welcome{left:100px;top:882px;font-size:18.5px;font-weight:300;color:#111}
.welcome span{color:var(--gold-text);font-weight:400}
.body-copy{left:101px;top:915px;width:560px;font-size:8.8px;line-height:11.7px;color:#222}
.body-copy p{margin-bottom:11.5px}
.read-more{left:99px;top:1112px;width:93px;height:29px;background:var(--gold);border:1px solid var(--gold-dark);font-size:10px;text-align:center;line-height:27px;border-radius:2px}
.fans{left:710px;top:679px;width:160px;height:322px;background:#eceef1;border:1px solid #dfe3e8;border-radius:2px}
.fans-top{position:absolute;left:10px;top:7px;font-size:9.5px;color:var(--navy);line-height:14px}
.fans-top small{font-size:8px}
.fans-like{position:absolute;right:6px;top:19px;width:32px;height:14px;border:1px solid #bbb;background:#f6f6f6;font-size:7px;text-align:right;padding-right:3px;line-height:12px;color:var(--navy)}
.fans-note{position:absolute;left:10px;top:47px;font-size:7.5px;color:#333}
.fans-note b{font-weight:500}
.face{position:absolute;width:40px;height:40px;background:linear-gradient(135deg,#c3aa94,#7d6a5c)}
.fname{position:absolute;width:40px;text-align:center;font-size:6.5px;color:#888}
.news{left:710px;top:1010px;width:160px;height:136px;background:#f0f0f0;border:1px solid var(--line)}
.news-head{height:25px;background:var(--bar);color:#fff;font-size:12px;line-height:25px;padding-left:12px}
.news-item{position:absolute;left:4px;width:150px;font-size:7.5px;line-height:10px;color:#222}
.news-item em{color:var(--gold-dark);font-size:7.3px}
.news-item u{display:block;text-align:right;font-size:6.5px;color:var(--gold-dark);font-style:italic;padding-right:4px;margin-top:2px}
.footer{left:0;top:1158px;width:968px;height:42px;background:var(--bar);color:#fff}
.foot-links{position:absolute;left:102px;top:9px;font-size:8.8px;line-height:13px}
.stay{position:absolute;left:625px;top:10px;font-size:15px;font-weight:300;font-style:italic}
.stay b{font-style:normal;font-weight:500}
.dot{position:absolute;top:11px;width:18px;height:18px;border-radius:50%}
</style>
</head>
<body>
<div class="abs topline"></div>
<header class="abs header"></header>
<div class="abs brand"><span class="brand-square"></span><span class="brand-name">DWELL VANTORO REAL ESTATE</span></div>
<div class="abs ask">If you have a question.<br>Please get in touch<span class="ask-btn">Click Here</span></div>
<div class="abs social-login"><span class="sq"><span></span></span><span class="lbl">Connect using <b>Chatterloop</b></span></div>

<nav>
  <div class="abs nav"></div>
  <div class="abs nav-tab">Home</div>
  <div class="abs nav-item" style="left:236px">Services</div>
  <div class="abs nav-item" style="left:353px">Portfolio</div>
  <div class="abs nav-item" style="left:471px">Goodies</div>
  <div class="abs nav-item" style="left:578px">Blog</div>
  <div class="abs search">search...<span class="search-btn"></span></div>
</nav>

<div class="abs hero" role="img" aria-label="Photo of a Florida house with palm trees and a family at the entrance"></div>
<form class="abs register">
  <div class="register-head"><i></i>Client Registration</div>
  <span class="field" style="top:112px;top:113px;top:114px;top:115px;top:114px;top:112px;top:113px;top:112px;top:113px;top:114px;top:115px;top:113px;top:114px;top:115px;top:114px;top:113px;top:115px;top:116px;top:115px;top:114px;top:113px;top:114px;top:115px;top:116px;top:115px;top:116px;top:115px;top:114px;top:115px;top:116px;top:115px;top:116px;top:115px;top:116px;top:115px;top:116px;top:115px;top:116px;top:115px;top:56px">USERNAME :</span>
  <span class="input" style="top:54px"></span>
  <span class="field" style="top:91px">EMAIL ADDRESS :</span>
  <span class="input" style="top:88px"></span>
  <span class="field" style="top:125px">PASSWORD :</span>
  <span class="input" style="top:122px"></span>
  <span class="field" style="top:160px">CONFIRM PASSWORD :</span>
  <span class="input" style="top:156px"></span>
  <span class="check" style="top:194px"><i></i>I have read and agree to the <u>terms and conditions.</u></span>
  <span class="check" style="top:213px"><i></i>Subscribe to <u>Newsletter.</u></span>
  <span class="reg-btn">REGISTER NOW</span>
</form>

<div class="abs ticker"><em>Lorem Ipsum</em> is simply dummy text of the printing and typesetting industry. <em>Lorem Ipsum has been the industry</em>'s standard dummy text ever since the 1500s,<br>when an unknown printer took a galley of type and scrambled it to make a type specimen book. It has survived not only five centuries, <em>but also the leap into</em></div>
<div class="abs like-btn"><i></i>Like</div>

<main class="abs content"></main>
<h2 class="abs h-featured">Featured Home For <span>Sale</span></h2>
<span class="abs arrow" style="left:91px;border-right:8px solid var(--gold)"></span>
<span class="abs arrow" style="left:866px;border-left:8px solid var(--gold)"></span>
<div class="abs thumb" style="left:105px;background:linear-gradient(135deg,#8aa86a,#3f6a2d)" role="img" aria-label="Photo of a white porch with hanging flowers"></div>
<div class="abs thumb" style="left:260px;background:linear-gradient(135deg,#cdd5dc,#7c8a94)" role="img" aria-label="Photo of a modern white villa"></div>
<div class="abs thumb" style="left:415px;background:linear-gradient(135deg,#d8cbb5,#8e7a63)" role="img" aria-label="Photo of a contemporary home with a rounded tower"></div>
<div class="abs thumb" style="left:570px;background:linear-gradient(135deg,#a9b6c4,#7a5c48)" role="img" aria-label="Photo of a brick family house with garage"></div>
<div class="abs thumb" style="left:724px;background:linear-gradient(135deg,#9fbfdd,#6f8a5a)" role="img" aria-label="Photo of a stone house with landscaped garden"></div>
<div class="abs cap" style="left:111px">Lorem Lipsum<small>Click to go »</small></div>
<div class="abs cap" style="left:264px">Lorem Lipsum<small>Click to go »</small></div>
<div class="abs cap" style="left:420px">Lorem Lipsum<small>Click to go »</small></div>
<div class="abs cap" style="left:576px">Lorem Lipsum<small>Click to go »</small></div>
<div class="abs cap" style="left:730px">Lorem Lipsum<small>Click to go »</small></div>

<section class="abs fore">
  <div class="fore-head"><i></i>FIND FORECLOSURES NEAR YOU</div>
  <p class="fore-text">Lorem Ipsum is simply dummy text of the printing and typesetting industry.</p>
  <span class="fin" style="top:87px;width:250px">City</span>
  <span class="fin" style="top:111px;width:250px">State</span>
  <span class="fin" style="top:134px;width:105px">Zip</span>
  <span class="fore-btn">Search</span>
  <span class="divider"></span>
  <div class="map" role="img" aria-label="Street map of the waterfront neighbourhood with highways"></div>
</section>

<h1 class="abs welcome">Welcome to <span>DWELL VANTORO REAL ESTATE</span></h1>
<div class="abs body-copy">
  <p>Lorem Ipsum is simply dummy text of the printing and typesetting industry. Lorem Ipsum has been the industry's standard dummy text ever since the 1500s, when an unknown printer took a galley of type and scrambled it to make a type specimen book.</p>
  <p>It has survived not only five centuries, but also the leap into electronic typesetting, remaining essentially unchanged. It was popularised in the 1960s with the release of Lettrix sheets containing Lorem Ipsum passages, and more recently with desktop publishing software like Pagecraft including versions of Lorem Ipsum.</p>
  <p>Contrary to popular belief, Lorem Ipsum is not simply random text. It has roots in a piece of classical Latin literature from 45 BC, making it over 2000 years old. Edwin Marlowe, a Latin professor at Ashgrove College in Virginia, looked up one of the more obscure Latin words, consectetur.</p>
  <p>From a Lorem Ipsum passage, and going through the cites of the word in classical literature, discovered the undoubtable source. Lorem Ipsum comes from sections 1.10.32 and 1.10.33 of "de Finibus Bonorum et Malorum" (The Extremes of Good and Evil) by Varrus, written in 45 BC. This book is a treatise on the theory of ethics, very popular during the Renaissance. The first line of Lorem Ipsum.</p>
</div>
<div class="abs read-more">Read More</div>

<aside class="abs fans">
  <div class="fans-top"><b style="font-weight:500">Dwell Vantoro</b> <small>On Chatterloop</small><br>1,056 People like</div>
  <span class="fans-like">Like</span>
  <div class="fans-note">637 people like <b>brightnest.</b></div>
  <span class="face" style="left:11px;top:66px" role="img" aria-label="Member photo"></span><span class="fname" style="left:11px;top:108px">Marisol</span>
  <span class="face" style="left:55px;top:66px" role="img" aria-label="Member photo"></span><span class="fname" style="left:55px;top:108px">tomek</span>
  <span class="face" style="left:100px;top:66px" role="img" aria-label="Member photo"></span><span class="fname" style="left:100px;top:108px">Orla</span>
  <span class="face" style="left:11px;top:129px" role="img" aria-label="Member photo"></span><span class="fname" style="left:11px;top:171px">Nana</span>
  <span class="face" style="left:55px;top:129px" role="img" aria-label="Member photo"></span><span class="fname" style="left:55px;top:171px">Carys</span>
  <span class="face" style="left:100px;top:129px" role="img" aria-label="Member photo"></span><span class="fname" style="left:100px;top:171px">Bruno</span>
  <span class="face" style="left:11px;top:193px" role="img" aria-label="Member photo"></span><span class="fname" style="left:11px;top:235px">Ivo</span>
  <span class="face" style="left:55px;top:193px" role="img" aria-label="Member photo"></span><span class="fname" style="left:55px;top:235px">pixel</span>
  <span class="face" style="left:100px;top:193px" role="img" aria-label="Member photo"></span><span class="fname" style="left:100px;top:235px">Linnea</span>
  <span class="face" style="left:11px;top:256px" role="img" aria-label="Member photo"></span><span class="fname" style="left:11px;top:298px">Nana</span>
  <span class="face" style="left:55px;top:256px" role="img" aria-label="Member photo"></span><span class="fname" style="left:55px;top:298px">Carys</span>
  <span class="face" style="left:100px;top:256px" role="img" aria-label="Member photo"></span><span class="fname" style="left:100px;top:298px">Bruno</span>
</aside>

<section class="abs news">
  <div class="news-head">News &amp; Events</div>
  <div class="news-item" style="top:30px"><em>13 APRIL, 2012</em><br>Lorem Ipsum is simply dummy text of the printing and typesetting<u>Read More</u></div>
  <div class="news-item" style="top:84px"><em>15 APRIL, 2012</em><br>Lorem Ipsum is simply dummy text of the printing and typesetting<u>Read More</u></div>
</section>

<footer class="abs footer">
  <div class="foot-links">Home Services &nbsp;Portfolio &nbsp;Goodies &nbsp;Blog<br>© Copyrights 2012 All rights Reserved</div>
  <div class="stay">let's stay <b>Connected!</b></div>
  <span class="dot" style="left:779px;background:#3aa7dd"></span>
  <span class="dot" style="left:803px;background:#1f74b0"></span>
  <span class="dot" style="left:827px;background:#e58a1f"></span>
  <span class="dot" style="left:851px;background:#d9d9d9"></span>
</footer>
</body>
</html>
```